Brand New Upscale OOBGYN Office

Im in Need of an advertising one sided postcard as soon as possible. It's for a brand new OBGYN office in the Northern Virginia area. We are trying to create a new patient customer base. I have attached photos of the inside of the office and logos. The office contact information needs to be on the postcard. You can find that on the attached pdf file named business card. That same file is the font that needs to be used. The font is called TT Drugs. Please contact me with any questions. I would appreciated it so much if you could send me these proofs as soon as possible. Thank you!!!
Women
Advertising
- TT Drugs

```html
<!DOCTYPE html>
<html lang="en">
<head>
<meta charset="utf-8">
<title>Northfield OBGYN – Postcard</title>
<link href="https://fonts.googleapis.com/css2?family=Raleway:wght@300;400&family=Roboto+Condensed:wght@700&family=Lato:wght@400;700&display=swap" rel="stylesheet">
<style>
  :root {
    --charcoal: #3a3a3b;
    --charcoal-deep: #2f2f30;
    --mint: #cfe0d6;
    --paper: #f4f4f4;
    --paper-shade: #dcdcdc;
    --ink-grey: #6b6b6d;
    --ink-dark: #2b2b2b;
    --logo-grey: #7b7b7e;
    --white: #ffffff;
    --soft-white: #d9d9d9;
    --photo-light: #ead6cc;
    --photo-mid: #c9a595;
    --photo-dark: #6e5449;
  }
  html, body {
    margin: 0;
    padding: 0;
    width: 1200px;
    height: 955px;
    overflow: hidden;
    background: var(--charcoal);
  }
  .postcard {
    position: relative;
    width: 1200px;
    height: 955px;
    overflow: hidden;
    font-family: "Lato", sans-serif;
  }
  .backdrop { position: absolute; inset: 0; }

  .brand-name {
    position: absolute;
    left: 287px;
    top: 52px;
    margin: 0;
    font-family: "Raleway", sans-serif;
    font-weight: 300;
    font-size: 62px;
    letter-spacing: 1px;
    color: var(--white);
    line-height: 1;
  }
  .brand-rule {
    position: absolute;
    left: 287px;
    top: 128px;
    width: 515px;
    height: 1px;
    background: var(--soft-white);
  }
  .brand-tagline {
    position: absolute;
    left: 287px;
    top: 136px;
    margin: 0;
    font-family: "Raleway", sans-serif;
    font-weight: 300;
    font-size: 42px;
    color: var(--soft-white);
    line-height: 1.1;
  }

  .headline {
    position: absolute;
    left: 55px;
    top: 420px;
    margin: 0;
    font-family: "Raleway", sans-serif;
    font-weight: 400;
    color: var(--ink-grey);
    line-height: 1;
  }
  .headline span { display: block; }
  .headline .lead { font-size: 50px; letter-spacing: 1px; }
  .headline .middle { font-size: 31px; margin-top: 12px; }
  .headline .close { font-size: 41px; margin-top: 12px; }

  .services-tab {
    position: absolute;
    left: 0;
    top: 598px;
    width: 308px;
    height: 50px;
    background: var(--charcoal);
    border-radius: 0 25px 25px 0;
    box-shadow: 0 8px 10px -6px rgba(0,0,0,0.35);
  }
  .services-tab h2 {
    margin: 0;
    padding-left: 40px;
    font-family: "Roboto Condensed", sans-serif;
    font-weight: 700;
    font-size: 30px;
    line-height: 50px;
    color: var(--white);
    letter-spacing: 0.5px;
  }
  .services-list {
    position: absolute;
    left: 55px;
    top: 670px;
    margin: 0;
    padding: 0;
    list-style: none;
  }
  .services-list li {
    position: relative;
    padding-left: 18px;
    font-weight: 700;
    font-size: 24px;
    line-height: 33px;
    color: var(--ink-dark);
  }
  .services-list li::before {
    content: "";
    position: absolute;
    left: 0;
    top: 13px;
    width: 8px;
    height: 8px;
    border-radius: 50%;
    background: var(--ink-grey);
  }

  .contact-list {
    position: absolute;
    left: 50px;
    top: 834px;
    margin: 0;
    padding: 0;
    list-style: none;
  }
  .contact-list li {
    display: flex;
    align-items: center;
    gap: 10px;
    font-size: 21px;
    line-height: 29px;
    color: var(--white);
  }
  .contact-list svg { width: 18px; height: 18px; flex: none; }
</style>
</head>
<body>
<main class="postcard">
  <svg class="backdrop" viewBox="0 0 1200 955" width="1200" height="955" aria-hidden="false">
    <defs>
      <linearGradient id="paperFade" x1="0" y1="0" x2="0.6" y2="1">
        <stop offset="0" stop-color="var(--paper-shade)"/>
        <stop offset="0.35" stop-color="var(--paper)"/>
        <stop offset="1" stop-color="var(--white)"/>
      </linearGradient>
      <linearGradient id="photoTone" x1="0" y1="0" x2="1" y2="1">
        <stop offset="0" stop-color="var(--photo-dark)"/>
        <stop offset="0.4" stop-color="var(--photo-mid)"/>
        <stop offset="0.75" stop-color="var(--photo-light)"/>
        <stop offset="1" stop-color="var(--photo-mid)"/>
      </linearGradient>
    </defs>

    <rect class="header-field" width="1200" height="955" fill="var(--charcoal)"/>

    <!-- mint wave band -->
    <path class="mint-wave" d="M0,300 C170,320 320,380 470,372 C700,360 930,240 1200,200 L1200,955 L0,955 Z" fill="var(--mint)"/>
    <!-- light panel -->
    <path class="light-panel" d="M0,330 C170,345 320,405 470,398 C700,388 930,262 1200,225 L1200,955 L0,955 Z" fill="url(#paperFade)"/>

    <!-- dark ribbon around image -->
    <path class="image-ribbon" d="M440,396 C560,330 900,250 1200,238 L1200,935 C1000,915 740,880 630,790 C520,700 470,540 440,396 Z" fill="var(--charcoal)"/>
    <!-- image area -->
    <path class="image-area" role="img" aria-label="Photo of a mother resting with her sleeping newborn baby" d="M480,400 C600,340 900,262 1200,252 L1200,905 C1010,890 770,850 665,770 C565,690 515,540 480,400 Z" fill="url(#photoTone)"/>

    <!-- bottom contact band -->
    <path class="contact-band" d="M0,828 C260,818 520,848 760,900 C880,926 980,944 1060,955 L0,955 Z" fill="var(--charcoal)"/>
    <path class="contact-edge" d="M0,822 C260,812 520,842 760,894 C920,928 1060,944 1200,948" fill="none" stroke="var(--paper-shade)" stroke-width="3"/>

    <!-- brand circle -->
    <circle class="brand-circle" cx="147" cy="148" r="115" fill="var(--logo-grey)"/>
  </svg>

  <h1 class="brand-name">NORTHFIELD OBGYN</h1>
  <div class="brand-rule"></div>
  <p class="brand-tagline">physicians &amp; midwives</p>

  <h2 class="headline">
    <span class="lead">CHOOSING</span>
    <span class="middle">THE RIGHT OBGYN</span>
    <span class="close">IS ESSENTIAL</span>
  </h2>

  <div class="services-tab"><h2>OUR SERVICES</h2></div>
  <ul class="services-list">
    <li>Obstetric and prenatal services</li>
    <li>Gynecologic services</li>
    <li>Surgical services</li>
    <li>Infertility services</li>
  </ul>

  <ul class="contact-list">
    <li>
      <svg viewBox="0 0 24 24" aria-hidden="true"><path d="M6.6 10.8a15.5 15.5 0 0 0 6.6 6.6l2.2-2.2a1 1 0 0 1 1-.25 11.4 11.4 0 0 0 3.6.57 1 1 0 0 1 1 1V20a1 1 0 0 1-1 1A17 17 0 0 1 3 4a1 1 0 0 1 1-1h3.5a1 1 0 0 1 1 1c0 1.25.2 2.45.57 3.57a1 1 0 0 1-.25 1z" fill="var(--soft-white)"/></svg>
      703-555-0142
    </li>
    <li>
      <svg viewBox="0 0 24 24" aria-hidden="true"><rect x="2" y="5" width="20" height="14" fill="var(--soft-white)"/><path d="M2 5l10 8 10-8" fill="none" stroke="var(--charcoal)" stroke-width="2"/></svg>
      info@northfieldobgyn.com
    </li>
    <li>
      <svg viewBox="0 0 24 24" aria-hidden="true"><circle cx="12" cy="12" r="10" fill="var(--soft-white)"/><path d="M2 12h20M12 2c3 3 3 17 0 20M12 2c-3 3-3 17 0 20" fill="none" stroke="var(--charcoal)" stroke-width="1.4"/></svg>
      www.northfieldobgyn.com
    </li>
  </ul>
</main>
</body>
</html>
```